Business Card Needed for Crafter of Pottery, Jewelry and Artwork

Calling all designers in search of an artistic challenge.

I need a new business card design for my pottery, jewelry and artwork business, Woven Glass and Tide, based in Vancouver BC.

I would like a card that is bright and inviting and preferably incorporates my logo and a sample of photos of my work while having a clean fresh look. The following contact details would preferably be included on the card as well:
• Helena Pikeworth
• Designer
• Phone: 604.555.0172
• Email: Designer@WovenGlassandTide.example
• Website: www.WovenGlassandTide.example
• Blog: www.ShapingHillside.example

The logo is attached in two color schemes in both Vector and Source formats. On past cards I’ve also included photos of my work. By including photos of the work the pieces are showcased and it catches people’s eye and prompts them to pick up the card and look at it more closely. For example, if I leave a stack in a coffee shop I want people to be drawn to the card, to pick it up and get a sense of the my product lines. Please feel free to pull photos of my work directly off of my website. If you need photos with higher pixels please let me know and I’ll email them directly to you. The website background is bffbda (191, 251, 218). I would like the business cards to match the feel of the website for consistency but the cards do not need to use the exact same colors. My website and current business card are predominantly turquoise shades. The background uses stripes provided by the website template. I don’t know the exact colors of the stripes.

My current business card is attached to show the use of photos in a design. Please note that I am not thrilled with my own design and am looking for variations and completely new designs. This example is not meant to be used as a template or starting point.

Here is some background surrounding my company:
WGT offers one of a kind jewelry, pottery, artwork and leather bags each designed with a twist. The pottery varies from rustic every day functional ware to raku artwork. The jewelry ranges from simple sterling every day pieces to multimedia pieces incorporating stone, metal, ceramics and fabric. The artwork is multimedia, typically acrylic paired with a natural element such as bark. All the bags are leather with reworked kimono fabric or patterned silk lining.

Feel free to check out my website to get a flavour for my work and the color scheme I've used on marketing materials so far. www.wovenglassandtide.example
Updates

Thank you to everyone who has submitted a design so far. I hope everyone has received some helpful feedback.

I'm going to post a survey to customers and friends asking for their votes. If you have new designs to submit please try to get them in by Saturday March 30 at noon so that I can include it in the survey launch.

Thank you

Target Market(s)

Females aged 25-65 interested in one of a kind functional pottery and jewelry.

Industry/Entity Type

Coffee Shop

Requirements
Must have
• Contact information, website, blog
Nice to have
• Logo, photos

```html
<!DOCTYPE html>
<html lang="en">
<head>
<meta charset="utf-8">
<title>Woven Glass and Tide — Business Card</title>
<link rel="stylesheet" href="https://fonts.googleapis.com/css2?family=Cinzel:wght@400;500&family=Cormorant+Garamond:wght@500&display=swap">
<style>
  :root {
    --navy: #23225a;
    --teal: #12b3a5;
    --white: #ffffff;
    --paper: #ffffff;
    --photo-light: #b9dcd6;
    --photo-mid: #9ccbc4;
  }
  * { box-sizing: border-box; margin: 0; padding: 0; }
  html, body {
    width: 1200px; height: 1200px; overflow: hidden;
    background: var(--paper);
  }
  .canvas { position: relative; width: 1200px; height: 1200px; }

  .card { position: absolute; width: 481px; height: 838px; overflow: hidden; }

  /* Front */
  .card-front { left: 72px; top: 172px; background: var(--white); }
  .photo-strip { position: absolute; left: 0; top: 56px; width: 481px; height: 122px; display: flex; }
  .photo { height: 100%; }
  .photo-vase { width: 126px; background: linear-gradient(180deg, var(--photo-light), #a9d3cc 70%, #e6efec); }
  .photo-necklace { width: 110px; background: linear-gradient(180deg, #c7ddd6, #a8a08e 55%, var(--photo-mid)); }
  .photo-mug { width: 122px; background: linear-gradient(180deg, var(--photo-light), #a9b9a8 55%, var(--photo-mid)); }
  .photo-pendant { width: 123px; background: linear-gradient(180deg, #c8dcd6, #b9b4a8 60%, var(--photo-light)); }

  .front-text {
    position: absolute; left: 0; width: 100%; text-align: center;
    font-family: 'Cinzel', serif; color: var(--navy);
  }
  .name { top: 236px; font-size: 36px; letter-spacing: 1px; }
  .role { top: 280px; font-size: 32px; letter-spacing: 1.5px; }
  .site-main {
    top: 328px; font-family: 'Cormorant Garamond', serif; font-weight: 500;
    font-size: 20px; color: var(--teal);
  }
  .contact {
    font-size: 17px; display: flex; justify-content: center; align-items: center; gap: 7px;
  }
  .contact svg { flex: none; }
  .phone {
    top: 387px; font-family: 'Cormorant Garamond', serif; font-weight: 500; font-size: 19px;
    font-variant-numeric: lining-nums;
  }
  .blog { top: 432px; }
  .email { top: 470px; }

  .pattern-band {
    position: absolute; left: 0; top: 571px; width: 481px; height: 267px;
    background: linear-gradient(90deg, var(--navy) 0%, #1c7f8a 35%, var(--teal) 50%, #1c7f8a 65%, var(--navy) 100%);
  }

  /* Back */
  .card-back { left: 588px; top: 203px; background: var(--navy); }
  .mark {
    position: absolute; left: 88px; top: 177px; width: 306px; height: 306px;
    border-radius: 50%; background: var(--white); border: 6px solid var(--teal);
    display: flex; align-items: center; justify-content: center; text-align: center;
  }
  .mark-name {
    font-family: 'Cinzel', serif; font-weight: 400; color: var(--navy);
    font-size: 30px; line-height: 1.25; letter-spacing: 2px;
  }
  .back-site {
    position: absolute; left: 0; top: 507px; width: 100%; text-align: center;
    font-family: 'Cinzel', serif; font-size: 20px; color: var(--white); letter-spacing: 0.5px;
  }
</style>
</head>
<body>
<main class="canvas">

  <section class="card card-front" aria-label="Card front">
    <div class="photo-strip">
      <div class="photo photo-vase" role="img" aria-label="Photo of a teal glazed pottery vase"></div>
      <div class="photo photo-necklace" role="img" aria-label="Photo of a chunky stone necklace on a display bust"></div>
      <div class="photo photo-mug" role="img" aria-label="Photo of handmade ceramic mugs"></div>
      <div class="photo photo-pendant" role="img" aria-label="Photo of a beaded necklace on a display bust"></div>
    </div>

    <p class="front-text name">Helena&nbsp; Pikeworth</p>
    <p class="front-text role">Designer</p>
    <p class="front-text site-main">www.WovenGlassandTide.example</p>

    <p class="front-text contact phone">
      <svg width="20" height="14" viewBox="0 0 20 14" aria-hidden="true">
        <path d="M2 5 Q10 -1 18 5 L15 7 L13 5 L7 5 L5 7 Z" fill="var(--teal)"/>
        <rect x="5" y="7" width="10" height="6" rx="1.5" fill="var(--teal)"/>
      </svg>
      604.555.0172
    </p>
    <p class="front-text contact blog">
      <svg width="15" height="15" viewBox="0 0 16 16" aria-hidden="true" fill="none" stroke="var(--teal)" stroke-width="1.2">
        <circle cx="8" cy="8" r="6.5"/><ellipse cx="8" cy="8" rx="3" ry="6.5"/><path d="M1.5 8h13M2.5 4.8h11M2.5 11.2h11"/>
      </svg>
      www.ShapingHillside.example
    </p>
    <p class="front-text contact email">
      <svg width="15" height="11" viewBox="0 0 16 11" aria-hidden="true" fill="none" stroke="var(--teal)" stroke-width="1.1">
        <rect x="0.6" y="0.6" width="14.8" height="9.8"/><path d="M0.6 0.6 L8 6.5 L15.4 0.6"/>
      </svg>
      Designer@WovenGlassandTide.example
    </p>

    <div class="pattern-band" role="img" aria-label="Decorative vertical stripe pattern in navy, turquoise and white"></div>
  </section>

  <section class="card card-back" aria-label="Card back">
    <div class="mark">
      <p class="mark-name">Woven Glass<br>and Tide</p>
    </div>
    <p class="back-site">www.WovenGlassandTide.example</p>
  </section>

</main>
</body>
</html>
```